Food manufacturer stationary
Business cards, envelopes, letterhead, cover sheet etc
Professional
Gustavo Arrieta
CEO
2875 North Clover Ave Salt Lake City, UT 84117
GUSTAVOJR@CORVANAFOODS.EXAMPLE
WWW.CORVANAMEXICANFOODS.EXAMPLE
Looking for something classy, professional, and modern. Something that says to client holding card this is a well established strong company

```html
<!DOCTYPE html>
<html lang="en">
<head>
<meta charset="utf-8">
<title>Corvana Business Cards</title>
<link href="https://fonts.googleapis.com/css2?family=Open+Sans:ital,wght@0,400;0,700;1,400&family=Michroma&display=swap" rel="stylesheet">
<style>
  :root{
    --backdrop:#e9e4dc;
    --card-light:#ffffff;
    --card-dark:#232121;
    --brown:#5a2c12;
    --gold:#c9a45a;
    --gold-light:#e8cf8e;
    --ink:#3a3a3a;
    --ink-light:#d8d2c4;
    --label:#3d3a36;
  }
  *{margin:0;padding:0;box-sizing:border-box}
  html,body{width:1200px;height:794px;overflow:hidden}
  body{background:var(--backdrop);font-family:"Open Sans",Arial,sans-serif;position:relative}
  .card{position:absolute;width:523px;height:336px;border-radius:14px;overflow:hidden;box-shadow:0 3px 8px rgba(0,0,0,.25)}
  .card--back{height:270px}
  .card--light{background:var(--card-light)}
  .card--dark{background:var(--card-dark)}
  .card__art{position:absolute;inset:0;width:100%;height:100%}
  .front-a{left:48px;top:43px}
  .front-b{left:632px;top:43px}
  .back-a{left:48px;top:468px}
  .back-b{left:632px;top:468px}
  .label{position:absolute;width:523px;text-align:center;font-family:"Michroma",sans-serif;font-size:19px;letter-spacing:2px;color:var(--label);text-transform:uppercase}
  .label-front-a{left:48px;top:395px}
  .label-front-b{left:632px;top:395px}
  .label-back-a{left:48px;top:752px}
  .label-back-b{left:632px;top:752px}
  .brand{position:absolute;display:flex;align-items:center;gap:10px}
  .brand__mark{width:34px;height:34px;border-radius:50%;background:var(--gold)}
  .brand__name{font-family:"Open Sans",sans-serif;font-weight:700;font-size:38px;color:var(--brown);letter-spacing:1px}
  .card--dark .brand__name{color:var(--gold)}
  .brand__sub{position:absolute;font-style:italic;font-size:12px;color:var(--brown)}
  .card--dark .brand__sub{color:var(--gold-light)}
  .front-a .brand,.front-b .brand{left:30px;top:138px}
  .front-a .brand__sub,.front-b .brand__sub{left:102px;top:190px}
  .card--back .brand{left:50%;top:106px;transform:translateX(-50%)}
  .card--back .brand__sub{left:0;right:0;text-align:center;top:158px}
  .contact{position:absolute;left:280px;top:52px;font-size:9.5px;line-height:1.55;color:var(--ink)}
  .card--dark .contact{color:var(--ink-light)}
  .contact__name{font-weight:700;font-size:12.5px;color:var(--brown)}
  .card--dark .contact__name{color:var(--gold-light)}
  .contact__title{font-style:italic;margin-bottom:12px}
  .contact__address{margin:0 0 16px}
  .contact__row{display:flex;align-items:center;gap:6px}
  .contact__row svg{width:8px;height:8px;flex:none}
</style>
</head>
<body>

<section class="card card--light front-a">
  <svg class="card__art" viewBox="0 0 523 336" aria-hidden="true">
    <path d="M465,0 C512,90 510,250 475,336 L523,336 L523,0 Z" fill="var(--brown)"/>
    <path d="M456,0 C503,90 501,250 466,336" fill="none" stroke="var(--gold)" stroke-width="2"/>
    <path d="M0,292 C70,320 150,332 240,336 L0,336 Z" fill="var(--brown)"/>
    <path d="M0,282 C70,312 150,327 250,334" fill="none" stroke="var(--gold)" stroke-width="2"/>
  </svg>
  <div class="brand"><span class="brand__mark"></span><span class="brand__name">Corvana</span></div>
  <div class="brand__sub">Mexican Foods, Inc.</div>
  <div class="contact">
    <div class="contact__name">Gustavo Arrieta</div>
    <div class="contact__title">CEO</div>
    <div class="contact__address">2875 North Clover Ave<br>Salt Lake City, UT 84117</div>
    <div class="contact__row"><svg viewBox="0 0 10 10"><circle cx="5" cy="5" r="5" fill="var(--brown)"/></svg>801-555-0142</div>
    <div class="contact__row"><svg viewBox="0 0 10 10"><circle cx="5" cy="5" r="5" fill="var(--brown)"/></svg>801-555-0187</div>
    <div class="contact__row"><svg viewBox="0 0 10 10"><circle cx="5" cy="5" r="5" fill="var(--brown)"/></svg>gustavojr@corvanafoods.example</div>
    <div class="contact__row"><svg viewBox="0 0 10 10"><circle cx="5" cy="5" r="5" fill="var(--brown)"/></svg>www.corvanamexicanfoods.example</div>
  </div>
</section>
<div class="label label-front-a">Business Card Front A</div>

<section class="card card--dark front-b">
  <svg class="card__art" viewBox="0 0 523 336" aria-hidden="true">
    <path d="M465,0 C512,90 510,250 475,336 L523,336 L523,0 Z" fill="var(--gold)"/>
    <path d="M0,292 C70,320 150,332 240,336 L0,336 Z" fill="var(--gold)"/>
  </svg>
  <div class="brand"><span class="brand__mark"></span><span class="brand__name">Corvana</span></div>
  <div class="brand__sub">Mexican Foods, Inc.</div>
  <div class="contact">
    <div class="contact__name">Gustavo Arrieta</div>
    <div class="contact__title">CEO</div>
    <div class="contact__address">2875 North Clover Ave<br>Salt Lake City, UT 84117</div>
    <div class="contact__row"><svg viewBox="0 0 10 10"><circle cx="5" cy="5" r="5" fill="var(--gold)"/></svg>801-555-0142</div>
    <div class="contact__row"><svg viewBox="0 0 10 10"><circle cx="5" cy="5" r="5" fill="var(--gold)"/></svg>801-555-0187</div>
    <div class="contact__row"><svg viewBox="0 0 10 10"><circle cx="5" cy="5" r="5" fill="var(--gold)"/></svg>gustavojr@corvanafoods.example</div>
    <div class="contact__row"><svg viewBox="0 0 10 10"><circle cx="5" cy="5" r="5" fill="var(--gold)"/></svg>www.corvanamexicanfoods.example</div>
  </div>
</section>
<div class="label label-front-b">Business Card Front B</div>

<section class="card card--light card--back back-a">
  <div class="brand"><span class="brand__mark"></span><span class="brand__name">Corvana</span></div>
  <div class="brand__sub">Mexican Foods, Inc.</div>
</section>
<div class="label label-back-a">Business Card Back A</div>

<section class="card card--dark card--back back-b">
  <div class="brand"><span class="brand__mark"></span><span class="brand__name">Corvana</span></div>
  <div class="brand__sub">Mexican Foods, Inc.</div>
</section>
<div class="label label-back-b">Business Card Back B</div>

</body>
</html>
```